Varen Psychiatry (Psychiatry clinic offering cutting edge treatments)

2 sided flyer for new psychiatry practice in Boulder, CO. I want something that looks professional, cutting edge, but also welcoming and friendly. My logo and pictures are attached.

Some of the copy:
Personalized, holistic Psychiatry combined with cutting-edge, evidence-based treatments. Our personalized psychiatry plan includes a bio-psycho-social evaluation, personalized treatment plan, medical evaluation for underlying hormonal and electrolyte abnormalities, and genetic testing (when warranted).

We specialize in treatment-resistant depression and substance abuse. We also treat PTSD, Bipolar Disorder, OCD, anxiety disorders, ADHD, and psychotic disorders.

About Dr. Pim- Dr. Pim served as Chief Resident at the largest private psychiatry hospital in Colorado. While there he won 3 consecutive awards for exceptionally high Psychiatry in service test score (99th percentile). He was a board member of Westfield Psychiatric Guild and helped advocate for better Colorado mental health policy. Dr. Pim is uniquely trained in Ketamine, Transcranial Magnetic Stimulation, and integrative psychiatry.

Target Market(s)

Private pay mental health patients, planning to give out to psychologists and family practice doctors

Industry/Entity Type

Medicine/Psychiatry

Colors
0054AA
0677BA
7BADD7
CADEEF
E8F1F8
0094D4
00A9DD
6FCCEA
C7EBF8
E9F6FB
00AB8E
00BBA5
67D7C9
C6EFE9
E9F9F6

Requirements
Must have
• My logo, an about me (Dr. Tom Pim) section

```html
<!DOCTYPE html>
<html lang="en">
<head>
<meta charset="utf-8">
<title>Varen Psychiatry – Two-Sided Flyer</title>
<link href="https://fonts.googleapis.com/css2?family=Montserrat:wght@400;500;600;700&family=Poppins:wght@600;700&display=swap" rel="stylesheet">
<style>
  :root{
    --backdrop:#939598;
    --white:#ffffff;
    --ink:#1e1e22;
    --logo-grey:#55565c;
    --navy:#0054AA;
    --blue:#0677BA;
    --sky:#0094D4;
    --cyan:#00A9DD;
    --teal:#00BBA5;
    --mint:#67D7C9;
    --ice:#C7EBF8;
    --black:#000000;
  }
  *{box-sizing:border-box;margin:0;padding:0}
  html,body{width:1200px;height:851px;overflow:hidden}
  body{background:var(--backdrop);position:relative;font-family:"Montserrat",sans-serif;color:var(--ink)}

  .page{position:absolute;top:101px;width:445px;height:630px;overflow:hidden}
  .page--front{left:154px;background:var(--white)}
  .page--back{left:638px;background:var(--black);color:var(--white)}

  .abs{position:absolute}
  .body-copy{font-size:8.3px;line-height:10.9px;text-align:justify;font-weight:400}

  /* front */
  .hero{left:0;top:0;width:445px;height:330px}
  .brand{left:22px;top:38px;display:flex;align-items:center;gap:8px}
  .brand__dot{width:26px;height:26px;border-radius:50%;background:var(--sky)}
  .brand__name{font-weight:600;font-size:19px;line-height:21px;color:var(--logo-grey);letter-spacing:1px;text-transform:uppercase;width:130px}
  .headline{left:33px;top:330px;width:400px;font-family:"Poppins",sans-serif;font-weight:700;font-size:17.6px;line-height:19.8px;text-transform:uppercase}
  .c-navy{color:var(--navy)}
  .c-sky{color:var(--sky)}
  .c-teal{color:var(--teal)}
  .front-photo{left:37px;top:380px;width:116px;height:159px;background:linear-gradient(160deg,#8d8a80,#c9c2b4 55%,#6f6a5c)}
  .front-copy{left:165px;top:378px;width:245px}
  .front-copy p+p{margin-top:10.9px}
  .front-copy em{font-weight:700}
  .front-deco{left:0;top:540px;width:210px;height:90px}
  .front-phone{left:190px;top:554px;width:220px;text-align:right;font-family:"Poppins",sans-serif;font-weight:700;font-size:28px;line-height:30px;background:linear-gradient(90deg,var(--navy),var(--sky) 55%,var(--teal));-webkit-background-clip:text;background-clip:text;color:transparent}
  .front-url{left:190px;top:586px;width:220px;text-align:right;font-size:11.6px;color:var(--blue);letter-spacing:.2px}
  .front-url b{font-weight:700}

  /* back */
  .back-top-deco{left:250px;top:0;width:195px;height:150px}
  .tms-photo{left:28px;top:28px;width:162px;height:156px;background:linear-gradient(135deg,#dfe6ee,#f3f6f9 50%,#b59273)}
  .back-intro{left:205px;top:25px;width:213px;font-size:8.5px;line-height:10.8px}
  .back-plan{left:28px;top:197px;width:390px;font-size:8.6px;line-height:10.8px}
  .bio-panel{left:89px;top:290px;width:332px;height:171px;border-radius:10px;background:linear-gradient(90deg,var(--navy),var(--sky) 50%,var(--cyan) 75%,var(--teal))}
  .portrait{left:19px;top:313px;width:132px;height:132px;border-radius:50%;border:4px solid var(--black);background:radial-gradient(circle at 50% 40%,#cfcfcf,#7b7b7b 70%,#4a4a4a)}
  .bio-copy{left:159px;top:306px;width:239px;font-size:7.9px;line-height:9.9px;color:var(--white)}
  .back-footer{left:0;top:460px;width:445px;height:170px}
  .back-brand{left:235px;top:513px;display:flex;align-items:center;gap:8px}
  .back-brand__dot{width:24px;height:24px;border-radius:50%;background:var(--white)}
  .back-brand__name{font-weight:600;font-size:18px;line-height:19px;color:var(--white);letter-spacing:1.2px;text-transform:uppercase;width:130px}
  .back-call{left:120px;top:564px;width:292px;text-align:right;font-size:21px;line-height:24px;color:var(--white);font-weight:400}
  .back-call b{font-family:"Poppins",sans-serif;font-weight:700}
  .back-url{left:120px;top:593px;width:292px;text-align:right;font-size:11px;letter-spacing:2.2px;color:var(--white)}
  .back-url b{font-weight:700}
</style>
</head>
<body>

<section class="page page--front">
  <svg class="abs hero" viewBox="0 0 445 330" aria-hidden="true">
    <defs>
      <linearGradient id="warm" x1="0" y1="0" x2="1" y2="1">
        <stop offset="0" stop-color="#f7f4f0"/>
        <stop offset=".55" stop-color="#e2d8cd"/>
        <stop offset="1" stop-color="#b8a999"/>
      </linearGradient>
      <linearGradient id="band" x1="0" y1="0" x2="1" y2="0">
        <stop offset="0" stop-color="#0054AA"/>
        <stop offset=".6" stop-color="#0677BA"/>
        <stop offset="1" stop-color="#0094D4"/>
      </linearGradient>
      <linearGradient id="heroDeco" x1="0" y1="1" x2="1" y2="0">
        <stop offset="0" stop-color="#0094D4" stop-opacity=".9"/>
        <stop offset="1" stop-color="#00A9DD" stop-opacity=".75"/>
      </linearGradient>
    </defs>
    <path d="M0 0H445V170C330 240 180 292 0 292Z" fill="url(#warm)" role="img" aria-label="Photo of a woman sitting by a window holding a smartphone"/>
    <path d="M0 292C180 292 330 240 445 170V186C330 258 180 314 0 316Z" fill="url(#band)"/>
    <path d="M262 300C300 290 350 270 400 240L445 210V300L430 290L400 312L330 316L290 312Z" fill="url(#heroDeco)" role="img" aria-label="Blue circuit-line decoration"/>
  </svg>

  <div class="abs brand">
    <span class="brand__dot"></span>
    <span class="brand__name">Varen Psychiatry</span>
  </div>

  <h1 class="abs headline">
    <span class="c-navy">Varen Psychiatry</span> <span class="c-sky">is now</span> <span class="c-teal">accepting</span><br>
    <span class="c-navy">new patients</span> <span class="c-sky">in Boulder,</span> <span class="c-teal">Colorado!</span>
  </h1>

  <div class="abs front-photo" role="img" aria-label="Photo of a therapist and patient talking in a bright lounge"></div>

  <div class="abs front-copy body-copy">
    <p><em>We specialize in</em> treating patients with treatment resistant depression and substance abuse disorders who have not responded to other forms of treatment. We also treat patients with PTSD, Bipolar Disorder, OCD, anxiety disorders, ADHD, and psychotic disorders. We believe that by providing comprehensive care, we can help our patients heal both emotionally and physically.</p>
    <p>We know that mental health is complex and that multiple factors can contribute to the development of mental illness. For this reason, we take an integrative approach that considers the whole person. We understand that each individual has their own unique set of experiences, strengths, and challenges, and we tailor our treatment plans to suit each patient’s personal needs.</p>
  </div>

  <svg class="abs front-deco" viewBox="0 0 210 90" role="img" aria-label="Cyan circuit-line decoration">
    <defs>
      <linearGradient id="frontDeco" x1="0" y1="1" x2="1" y2="0">
        <stop offset="0" stop-color="#0094D4"/>
        <stop offset="1" stop-color="#00BBA5"/>
      </linearGradient>
    </defs>
    <path d="M0 50L40 20L90 0L140 15L175 45L210 70V90H0Z" fill="url(#frontDeco)" opacity=".85"/>
  </svg>

  <div class="abs front-phone">555-014-2290</div>
  <div class="abs front-url">WWW.<b>VARENPSYCHIATRY</b>.COM</div>
</section>

<section class="page page--back">
  <div class="abs back-top-deco" role="img" aria-label="Faint dark-blue circuit-line decoration" style="background:linear-gradient(200deg,rgba(0,84,170,.35),rgba(0,84,170,0) 70%)"></div>

  <div class="abs tms-photo" role="img" aria-label="Photo of a patient receiving transcranial magnetic stimulation beside the treatment machine"></div>

  <p class="abs back-intro body-copy">So often, when we think about mental health, we focus on just treating symptoms. If someone is depressed, they might take medication to help them feel better. If someone is anxious, they might see a therapist to help them manage their anxiety. While these treatments can be helpful, they only address the symptoms of mental illness. To truly address mental health, it is necessary to treat the root causes. This might involve addressing childhood trauma, unresolved conflict, or feelings of worthlessness. It might also involve developing healthy coping mechanisms and learning how to set boundaries. By treating the root causes of mental illness, we can begin to create lasting change.</p>

  <p class="abs back-plan body-copy">Our personalized psychiatry plan includes a bio-psycho-social evaluation, tailored treatment plan, medical evaluation for underlying hormonal and electrolyte abnormalities, and genetic testing (when warranted). Our integrative psychiatry approach combines cutting edge, evidence-based treatments with holistic therapies to provide you with the best possible care. In addition, we also offer Ketamine Assisted Therapy, TMS (Transcranial Magnetic Simulation), and MAT Treatment for Substance abuse. We pride ourselves on always staying up to date on the latest mental health treatments.</p>

  <div class="abs bio-panel"></div>
  <div class="abs portrait" role="img" aria-label="Black and white portrait of Dr. Tom Pim"></div>
  <p class="abs bio-copy body-copy">Dr. Tom Pim is a psychiatrist with years of experience providing compassionate, evidence-based care to patients of all ages. He is uniquely trained in several cutting-edge treatments, including Ketamine, Transcranial Magnetic Stimulation (TMS), and integrative psychiatry. Prior to founding Varen Psychiatry, Dr. Pim served as Chief Resident at the largest private psychiatry hospital in Colorado. While there, he won three consecutive awards for exceptionally high Psychiatry in-service test scores (99th percentile). In addition, he was a board member of the Westfield Psychiatric Guild and helped advocate for better Colorado mental health policy. Thanks to his extensive training and experience, Dr. Pim is able to provide each patient with an individualized treatment plan that brings optimum results.</p>

  <svg class="abs back-footer" viewBox="0 0 445 170" aria-hidden="true">
    <defs>
      <linearGradient id="footBand" x1="0" y1="0" x2="1" y2="0">
        <stop offset="0" stop-color="#0054AA"/>
        <stop offset="1" stop-color="#0677BA"/>
      </linearGradient>
      <linearGradient id="footEdge" x1="0" y1="0" x2="1" y2="0">
        <stop offset="0" stop-color="#0094D4"/>
        <stop offset="1" stop-color="#00BBA5"/>
      </linearGradient>
      <linearGradient id="footDeco" x1="0" y1="1" x2="1" y2="0">
        <stop offset="0" stop-color="#00A9DD"/>
        <stop offset="1" stop-color="#0094D4"/>
      </linearGradient>
    </defs>
    <path d="M0 130L30 95L80 60L130 35L190 15L225 20L200 48L130 80L60 118L0 150Z" fill="url(#footDeco)" opacity=".9" role="img" aria-label="Blue circuit-line decoration"/>
    <path d="M0 147C120 80 260 40 445 39V170H0Z" fill="url(#footBand)"/>
    <path d="M0 147C120 80 260 40 445 39V49C260 50 120 88 0 156Z" fill="url(#footEdge)"/>
  </svg>

  <div class="abs back-brand">
    <span class="back-brand__dot"></span>
    <span class="back-brand__name">Varen Psychiatry</span>
  </div>
  <div class="abs back-call">CALL US: <b>555-014-2290</b></div>
  <div class="abs back-url">WWW.<b>VARENPSYCHIATRY</b>.COM</div>
</section>

</body>
</html>
```